Medical Device Packaging Project 4 of 5

We are a medical device startup company needing packaging for a total of 5 device brands. This is posting 4 of 5 and the device name is "Velotin"

Velotin is an intraocular lens for use in cataract surgery. The target market is Chinese ophthalmologists. The box should be sophisticated and upmarket.

The company name is Cendra Optics, I have included the logo in the uploaded files section. You should include the logo on the box.

I have uploaded a sample lens boxes from other companies that demonstrate the information needed to be contained on the box in terms of address, warnings, symbols, etc.

I have also uploaded the blank dieline of the boxes

You are welcome and encouraged to also submit to projects 1, 2, 3, and 5 as well. The same rules and expectations apply.

Industry/Entity Type

It Company

Requirements
Should not have
• Should not have any images of an eye or any bionic/futuristic feel to the design
• Note that the halvisen box is for text reference only. You may use the lens image but the futuristic/bionic look is NOT what we are going for with this brand. It should be traditional upmarket medical device artwork.

```html
<!DOCTYPE html>
<html lang="en">
<head>
<meta charset="utf-8">
<title>Velotin Carton Dieline</title>
<link href="https://fonts.googleapis.com/css2?family=Fira+Sans+Condensed:wght@600;700&family=Arimo:wght@400;700&display=swap" rel="stylesheet">
<style>
  :root {
    --bg: #000000;
    --green: #34a828;
    --white: #ffffff;
    --navy: #1f3f8f;
    --ink: #222222;
  }
  html, body { margin: 0; padding: 0; overflow: hidden; background: var(--bg); }
  .canvas { display: block; width: 1071px; height: 1200px; }
  .fill-green { fill: var(--green); }
  .fill-white { fill: var(--white); }
  .product-name { font-family: "Fira Sans Condensed", sans-serif; font-weight: 700; font-size: 74px; fill: var(--green); }
  .product-sub { font-family: "Arimo", sans-serif; font-weight: 700; font-size: 9.6px; fill: var(--green); }
  .flap-claim { font-family: "Arimo", sans-serif; font-weight: 700; font-size: 12.5px; fill: var(--green); }
  .brand { font-family: "Arimo", sans-serif; font-weight: 700; letter-spacing: 1px; fill: var(--navy); }
  .brand-white { fill: var(--white); }
  .maker { font-family: "Arimo", sans-serif; font-size: 9.2px; fill: var(--ink); }
  .info { font-family: "Arimo", sans-serif; font-size: 8.8px; fill: var(--white); }
  .icon-line { fill: none; stroke-width: 1.6; }
  .icon-green { stroke: var(--green); }
  .icon-white { stroke: var(--white); }
  .badge-text { font-family: "Arimo", sans-serif; font-weight: 700; font-size: 8px; }
</style>
</head>
<body>
<svg class="canvas" viewBox="0 0 1071 1200" xmlns="http://www.w3.org/2000/svg">
  <defs>
    <clipPath id="main-panel-clip">
      <rect x="35" y="190" width="1003" height="385" rx="16"/>
    </clipPath>
  </defs>

  <!-- top tuck flap -->
  <g class="top-flap">
    <polygon class="fill-green" points="134,68 262,38 810,38 938,68 938,172 826,172 812,190 262,190 248,172 134,172"/>
    <g class="maker">
      <text x="718" y="138" transform="rotate(180 718 138)">Northvale Optical Systems Ltd.</text>
      <text x="718" y="126" transform="rotate(180 718 126)">Arden House, Arden Avenue, Kelbridge, Westshire. KB4 2PQ, UK</text>
      <text x="718" y="114" transform="rotate(180 718 114)">Website: www.nv-optic.com &#160;&#160; E-mail: info@nv-optic.com</text>
      <text x="718" y="82" transform="rotate(180 718 82)">REV.06 NVS03062015</text>
    </g>
  </g>

  <!-- main front panel -->
  <g class="main-panel">
    <rect class="fill-white" x="35" y="190" width="1003" height="385" rx="16"/>
    <path class="fill-green" clip-path="url(#main-panel-clip)"
      d="M158,190 Q360,520 1038,496 L1038,470 Q480,480 306,328 Q520,208 810,190 Z"/>
    <text class="product-name" x="624" y="348" text-anchor="middle">Velotin</text>
    <text class="product-sub" x="624" y="366" text-anchor="middle">HYDROPHOBIC ACRYLIC INTRAOCULAR LENS</text>

    <g class="brand-mark">
      <circle cx="374" cy="512" r="4" fill="var(--navy)"/>
      <text class="brand" x="384" y="518" font-size="17">Cendra Optics</text>
    </g>
    <text class="brand" x="182" y="412" font-size="12" text-anchor="middle" transform="rotate(90 182 412)">Cendra Optics</text>
    <text class="brand" x="928" y="542" font-size="10" text-anchor="middle" transform="rotate(-90 928 542)">Cendra Optics</text>

    <!-- symbols column -->
    <g class="symbols-side">
      <circle class="icon-line icon-green" cx="920" cy="262" r="12"/>
      <line class="icon-line icon-green" x1="912" y1="254" x2="928" y2="270"/>
      <circle class="icon-line icon-green" cx="920" cy="297" r="12"/>
      <line class="icon-line icon-green" x1="912" y1="289" x2="928" y2="305"/>
      <circle class="icon-line icon-green" cx="920" cy="331" r="12"/>
      <text class="badge-text" x="920" y="335" fill="var(--green)" text-anchor="middle" font-size="12">2</text>
      <line class="icon-line icon-green" x1="912" y1="323" x2="928" y2="339"/>
      <polygon fill="var(--green)" points="920,348 934,376 906,376"/>
      <text class="badge-text" x="920" y="373" fill="var(--white)" text-anchor="middle" font-size="13">!</text>
      <rect x="912" y="383" width="18" height="54" rx="9" fill="var(--green)"/>
      <text class="badge-text" x="925" y="410" fill="var(--white)" text-anchor="middle" transform="rotate(-90 925 410)">STERILE EO</text>
    </g>
  </g>

  <!-- lower dust flap -->
  <g class="lower-flap">
    <polygon class="fill-white" points="134,592 248,592 262,575 810,575 826,592 938,592 938,700 810,725 262,725 134,700"/>
    <circle cx="318" cy="652" r="4" fill="var(--navy)"/>
    <text class="brand" x="328" y="658" font-size="17">Cendra Optics</text>
    <text class="flap-claim" x="470" y="656">HYDROPHOBIC ACRYLIC INTRAOCULAR LENS</text>
    <text class="flap-claim" x="470" y="673">ASPHERIC WITH 360° SQUARE EDGE</text>
  </g>

  <!-- back panel -->
  <g class="back-panel">
    <polygon class="fill-green" points="262,725 810,725 810,1112 806,1162 266,1162 262,1112"/>
    <circle cx="350" cy="904" r="4" fill="var(--white)"/>
    <text class="brand brand-white" x="360" y="910" font-size="18">Cendra Optics</text>

    <g class="info">
      <text x="551" y="794">Contains one sterile intraocular lens</text>
      <text x="551" y="803">Do not use if the packaging is damaged</text>
      <text x="551" y="812">Do not resterilize</text>
      <text x="551" y="828">Bevat één steriele intraoculaire lens</text>
      <text x="551" y="837">Niet gebruiken als de verpakking beschadigd is</text>
      <text x="551" y="846">Niet opnieuw steriliseren</text>
      <text x="551" y="861">Contient une lentille intraoculaire stérile</text>
      <text x="551" y="870">Ne pas utiliser si l'emballage est endommagé</text>
      <text x="551" y="879">Ne pas restériliser</text>
      <text x="551" y="894">Enthält eine sterile intraokulare Linse</text>
      <text x="551" y="903">Nicht verwenden, wenn die Verpackung beschädigt ist</text>
      <text x="551" y="912">Nicht resterilisieren</text>
      <text x="551" y="928" font-size="7.6">Periéchei éna aposteiroméno endofthálmia fakó OR</text>
      <text x="551" y="937" font-size="7.6">Περιέχει ένα αποστειρωμένο ενδοφθάλμια φακό</text>
      <text x="551" y="946" font-size="7.6">Μην το χρησιμοποιείτε εάν η συσκευασία έχει υποστεί ζημιά</text>
      <text x="551" y="955" font-size="7.6">OR Min to chrisimopoieíte eán i syskevasía échei ypostei zimiá</text>
      <text x="551" y="964" font-size="7.6">Μην επαναποστειρώνετε &#160;OR Min epanaposteirónete</text>
      <text x="551" y="980">Contiene una lente intraoculare sterile</text>
      <text x="551" y="989">Non usare se la confezione è danneggiata</text>
      <text x="551" y="998">Non risterilizzare</text>
      <text x="551" y="1013">Contém uma lente intra-ocular esterilizada</text>
      <text x="551" y="1022">Não use se a embalagem está danificada</text>
      <text x="551" y="1031">Não reesterilize</text>
      <text x="551" y="1047">Contiene una lente intraocular estéril</text>
      <text x="551" y="1056">No utilizar si el envase está dañado</text>
      <text x="551" y="1065">No vuelva a esterilizar</text>
    </g>

    <g class="symbols-back">
      <rect x="311" y="1045" width="56" height="15" rx="7.5" fill="var(--white)"/>
      <text class="badge-text" x="339" y="1056" fill="var(--green)" text-anchor="middle">STERILE EO</text>
      <polygon fill="var(--white)" points="385,1038 400,1066 370,1066"/>
      <text class="badge-text" x="385" y="1063" fill="var(--green)" text-anchor="middle" font-size="13">!</text>
      <circle class="icon-line icon-white" cx="416" cy="1052" r="12"/>
      <text class="badge-text" x="416" y="1056" fill="var(--white)" text-anchor="middle" font-size="12">2</text>
      <line class="icon-line icon-white" x1="408" y1="1044" x2="424" y2="1060"/>
      <circle class="icon-line icon-white" cx="451" cy="1052" r="12"/>
      <line class="icon-line icon-white" x1="443" y1="1044" x2="459" y2="1060"/>
      <circle class="icon-line icon-white" cx="485" cy="1052" r="12"/>
      <line class="icon-line icon-white" x1="477" y1="1044" x2="493" y2="1060"/>
    </g>
  </g>
</svg>
</body>
</html>
```